Harvest Ledger Group
Business Cards, Envelopes and Letterhead
Project: Harvest Ledger Group
Harvest Ledger Group -
Creative Brief
Bright & Fun-filled
Marcus T. Halvorsen
President
47 Brookmere Loop West, Suite B318 Englewood, CO 80214
mh@kt-assetpartners.com
www.kt-assetpartners.com

```html
<!DOCTYPE html>
<html lang="en">
<head>
<meta charset="utf-8">
<title>Harvest Ledger Group – Stationery</title>
<link href="https://fonts.googleapis.com/css2?family=Libre+Baskerville:wght@700&family=Open+Sans:wght@400;600&display=swap" rel="stylesheet">
<style>
:root{
  --bg-dark:#7f7f7f;
  --bg-light:#a3a3a3;
  --paper:#ffffff;
  --navy:#0b2a63;
  --blue:#1553b8;
  --blue-light:#6fa0e8;
  --text:#4a4a4a;
  --faint:#e4ebf5;
}
*{margin:0;padding:0;box-sizing:border-box}
html,body{width:1200px;height:626px;overflow:hidden}
body{
  position:relative;
  background:radial-gradient(ellipse at 50% 45%,var(--bg-light),var(--bg-dark));
  font-family:"Open Sans",Arial,sans-serif;color:var(--text);
}
.sheet{position:absolute;background:var(--paper);box-shadow:0 2px 6px rgba(0,0,0,.35);overflow:hidden}
.band{position:absolute;top:0;bottom:0;background:linear-gradient(90deg,var(--navy),var(--blue) 60%,var(--blue-light))}
.brand{position:absolute;display:flex;align-items:center;gap:5px;font-family:"Libre Baskerville",Georgia,serif;font-weight:700;color:var(--navy);white-space:nowrap}
.brand-mark{background:var(--blue);flex:none}
.faint-mark{position:absolute;background:var(--faint);opacity:.8}
.contact{position:absolute;font-size:5px;line-height:7px;color:var(--text);white-space:nowrap}

/* business card front */
.card-front{left:34px;top:197px;width:163px;height:101px}
.card-front .brand{left:0;right:0;top:42px;justify-content:center;font-size:8px}
.card-front .brand-mark{width:10px;height:10px}

/* business card back */
.card-back{left:34px;top:307px;width:163px;height:103px}
.card-back .band{left:0;width:8px}
.card-back .contact{left:16px;top:46px;font-size:4px;line-height:6px}
.card-back .person{position:absolute;right:12px;top:62px;text-align:right;font-size:5px;line-height:7px}
.person-name{color:var(--navy);font-weight:600}

/* letterhead */
.letterhead{left:233px;top:29px;width:415px;height:564px}
.letterhead .band{left:0;width:20px}
.letterhead .brand{left:36px;top:30px;font-size:11px}
.letterhead .brand-mark{width:24px;height:24px}
.letterhead .faint-mark{right:40px;bottom:40px;width:130px;height:120px}
.letterhead .contact{left:36px;bottom:14px;display:flex;gap:10px}

/* envelope back */
.envelope-back{left:679px;top:79px;width:495px;height:245px}
.envelope-back svg{position:absolute;left:0;top:0}

/* envelope front */
.envelope-front{left:679px;top:334px;width:495px;height:252px}
.envelope-front .band{left:0;width:16px}
.envelope-front .brand{left:30px;top:18px;font-size:10px}
.envelope-front .brand-mark{width:22px;height:22px}
.envelope-front .faint-mark{right:40px;bottom:30px;width:110px;height:105px}
.envelope-front .contact{left:30px;bottom:20px;display:flex;gap:10px}
</style>
</head>
<body>

<section class="sheet card-front" aria-label="Business card front">
  <div class="brand"><span class="brand-mark"></span>Harvest Ledger Group</div>
</section>

<section class="sheet card-back" aria-label="Business card back">
  <div class="band"></div>
  <div class="contact">
    P: (303) 555-0142<br>F: (303) 555-0143<br>
    mh@harvestledger.example<br>www.harvestledger.example<br>
    47 Brookmere Loop West, Suite B318<br>Larkmoor, OR 97999
  </div>
  <div class="person"><div class="person-name">Marcus T. Halvorsen</div><div>President</div></div>
</section>

<section class="sheet letterhead" aria-label="Letterhead">
  <div class="band"></div>
  <div class="brand"><span class="brand-mark"></span>Harvest Ledger Group</div>
  <div class="faint-mark" role="img" aria-label="Faint brand decoration"></div>
  <div class="contact">
    <div>P: (303) 555-0142<br>F: (303) 555-0143<br>C: (303) 555-0199</div>
    <div>mh@harvestledger.example<br>www.harvestledger.example<br>47 Brookmere Loop West, Suite B318 Larkmoor, OR 97999</div>
  </div>
</section>

<section class="sheet envelope-back" aria-label="Envelope back">
  <svg width="495" height="245" viewBox="0 0 495 245">
    <defs>
      <linearGradient id="flap-fill" x1="0" y1="0" x2="0" y2="1">
        <stop offset="0" stop-color="#0b2a63"/>
        <stop offset=".6" stop-color="#1553b8"/>
        <stop offset="1" stop-color="#6fa0e8"/>
      </linearGradient>
    </defs>
    <path d="M0 0H495V55C430 60 340 95 247 95C154 95 65 60 0 55Z" fill="url(#flap-fill)"/>
    <path d="M0 55C65 60 154 95 247 95C340 95 430 60 495 55" fill="none" stroke="#d8d8d8" stroke-width="1"/>
  </svg>
</section>

<section class="sheet envelope-front" aria-label="Envelope front">
  <div class="band"></div>
  <div class="brand"><span class="brand-mark"></span>Harvest Ledger Group</div>
  <div class="faint-mark" role="img" aria-label="Faint brand decoration"></div>
  <div class="contact">
    <div>P: (303) 555-0142<br>F: (303) 555-0143<br>C: (303) 555-0199</div>
    <div>mh@harvestledger.example<br>www.harvestledger.example<br>47 Brookmere Loop West, Suite B318 Larkmoor, OR 97999</div>
  </div>
</section>

</body>
</html>
```